Vendrick Legal PLLC updated letterhead for solo law practice - legal/professional services

I need a new letterhead design on a word document for my solo law practice. I have attached my current letterhead. Here is my company info:

Dorian Vendrick
Vendrick Legal PLLC
2718 Brambleton, Suite 430
Dallas, Texas 75291
Phone: 214 555 0187
Email: dorian@vendrick-legal.example
Website: www.vendrick-legal.example

Preferably I'd like the logo on top followed by my name and email (in the header)

At the bottom (footer) i'd like the rest of the information.

I am fine using a color for the line in between "Vendrick" and "Legal" in the "Vendrick Legal" logo. Or a different font.

Industry/Entity Type

Legal

Font styles to use
Serif

Colors

Designer to choose only greyscale colors for use in the design.

Requirements
Must have
• The "Vendrick Legal" logo with the line in between "Vendrick" and "Legal" but I am open to ideas on structure and color schemes.
Nice to have
• Logo on top with new color scheme, along with my name and email.
• Address, phone number, web address on bottom.

```html
<!DOCTYPE html>
<html lang="en">
<head>
<meta charset="utf-8">
<title>Vendrick Legal PLLC — Letterhead</title>
<link rel="stylesheet" href="https://fonts.googleapis.com/css2?family=Cinzel:wght@400&family=PT+Sans:wght@400&display=swap">
<style>
  :root {
    --backdrop: #58585b;
    --paper: #ffffff;
    --plum: #6e5a72;
    --gold: #d3ae68;
    --slate: #6f6f71;
    --ink: #2b2b2b;
    --mid-grey: #77777a;
  }
  * { margin: 0; padding: 0; box-sizing: border-box; }
  html, body {
    width: 1200px;
    height: 894px;
    overflow: hidden;
    background: var(--backdrop);
  }
  .sheet {
    position: absolute;
    top: 137px;
    height: 619px;
    background: var(--paper);
  }
  .sheet--colour { left: 116px; width: 437px; }
  .sheet--mono { left: 622px; width: 462px; }

  .letterhead {
    position: absolute;
    top: 36px;
    left: 0;
    right: 0;
    display: flex;
    justify-content: center;
    align-items: flex-start;
    gap: 14px;
  }
  .brand-square {
    width: 43px;
    height: 43px;
    flex: none;
  }
  .brand-block {
    display: flex;
    flex-direction: column;
    align-items: center;
  }
  .firm-name {
    font-family: "Cinzel", serif;
    font-size: 20px;
    line-height: 20px;
    letter-spacing: 0.2px;
    white-space: nowrap;
  }
  .entity-rule {
    display: flex;
    align-items: center;
    gap: 3px;
    width: 150px;
    margin-top: 1px;
  }
  .entity-rule .rule {
    flex: 1;
    height: 0.6px;
  }
  .entity-rule .entity {
    font-family: "Cinzel", serif;
    font-size: 7px;
    letter-spacing: 2.6px;
    line-height: 8px;
  }
  .contact-line {
    display: flex;
    align-items: center;
    margin-top: 3px;
    font-family: "PT Sans", sans-serif;
    font-size: 9.5px;
    white-space: nowrap;
  }
  .contact-line .divider {
    width: 0.7px;
    height: 12px;
    margin: 0 4px;
  }

  .footer {
    position: absolute;
    top: 563px;
    left: 0;
    right: 0;
    text-align: center;
    font-family: "PT Sans", sans-serif;
    font-size: 9px;
    line-height: 11.3px;
  }

  /* Colour edition */
  .sheet--colour .brand-square { background: var(--plum); }
  .sheet--colour .firm-name { color: var(--plum); }
  .sheet--colour .entity { color: var(--plum); }
  .sheet--colour .rule { background: var(--plum); }
  .sheet--colour .contact-line { color: var(--plum); }
  .sheet--colour .divider { background: var(--gold); }
  .sheet--colour .footer { color: var(--ink); }

  /* Greyscale edition */
  .sheet--mono .brand-square { background: var(--slate); }
  .sheet--mono .firm-name,
  .sheet--mono .entity,
  .sheet--mono .contact-line { color: var(--slate); }
  .sheet--mono .rule,
  .sheet--mono .divider { background: var(--slate); }
  .sheet--mono .footer { color: var(--mid-grey); }
</style>
</head>
<body>

  <section class="sheet sheet--colour" aria-label="Letterhead, colour edition">
    <header class="letterhead">
      <div class="brand-square"></div>
      <div class="brand-block">
        <div class="firm-name">VENDRICK LEGAL</div>
        <div class="entity-rule"><span class="rule"></span><span class="entity">PLLC</span><span class="rule"></span></div>
        <div class="contact-line">
          <span class="person">Dorian Vendrick</span>
          <span class="divider"></span>
          <span class="email">dorian@vendrick-legal.example</span>
        </div>
      </div>
    </header>
    <footer class="footer">
      <p>2718 Brambleton, Suite 430 Dallas, Texas 75291</p>
      <p>www.vendrick-legal.example</p>
      <p>214 555 0187</p>
    </footer>
  </section>

  <section class="sheet sheet--mono" aria-label="Letterhead, greyscale edition">
    <header class="letterhead">
      <div class="brand-square"></div>
      <div class="brand-block">
        <div class="firm-name">VENDRICK LEGAL</div>
        <div class="entity-rule"><span class="rule"></span><span class="entity">PLLC</span><span class="rule"></span></div>
        <div class="contact-line">
          <span class="person">Dorian Vendrick</span>
          <span class="divider"></span>
          <span class="email">dorian@vendrick-legal.example</span>
        </div>
      </div>
    </header>
    <footer class="footer">
      <p>2718 Brambleton, Suite 430 Dallas, Texas 75291</p>
      <p>www.vendrick-legal.example</p>
      <p>214 555 0187</p>
    </footer>
  </section>

</body>
</html>
```